Coffee Cocktails Recipe Flips cards

create (12) recipe cards that illustrate the finished beverage, with its description, ingredients, and instructions. each card should be 5"x7" and styled to incorporate brand theme and the cultural elements of the beverage. cards will be used for stuffers in shipments of product, used by bartenders, and digitally shared. Present each drink in glassware that embodies the spirit of the culture it represents, garnishing with flair and a nod to the exotic origins, creating a multisensory experience that'll transport the drinker to distant lands with just one indulgent sip.
The presentation of each drink should reflect the cultural fusion aesthetically, using suggested glassware and garnishes to bring the exotic themes to life. Enjoy crafting these drinks and take your guests on a flavorful voyage around the world with each sip!

Target Market(s)

Consumers and Bars and Restaurants

Industry/Entity Type

coffee and adult beverages

Colors

Designer to choose colors to be used in the design.

Requirements
Must have
• brand alignment, styled to reflect the uniqueness of each recipe
Should not have
• appropriate glassware, garnishments, and images of raw ingredients

```html
<!DOCTYPE html>
<html lang="en">
<head>
<meta charset="utf-8">
<title>Café Mocha Bliss – Recipe Card</title>
<link rel="stylesheet" href="https://fonts.googleapis.com/css2?family=Inter:wght@400;500;700&family=Merriweather:ital,wght@1,700;1,900&display=swap">
<style>
  :root {
    --stage: #666666;
    --navy: #141d26;
    --ink: #0b0f12;
    --green: #10a87a;
    --green-deep: #0c7e5f;
    --mint: #1ee3a0;
    --white: #ffffff;
    --text-dark: #1f2428;
    --rule: rgba(255,255,255,0.55);
    --photo-dark: #1f1b18;
    --photo-mid: #4a3c31;
    --photo-light: #cfcac4;
  }
  * { box-sizing: border-box; margin: 0; padding: 0; }
  html, body { width: 705px; height: 1200px; overflow: hidden; }
  body {
    background: var(--stage);
    font-family: "Inter", Arial, sans-serif;
    display: flex;
    flex-direction: column;
    align-items: center;
    gap: 20px;
    padding-top: 20px;
  }
  .card {
    position: relative;
    width: 408px;
    height: 570px;
    overflow: hidden;
    box-shadow: 0 10px 24px rgba(0,0,0,0.35);
  }

  /* ---------- Front ---------- */
  .card--front {
    background: linear-gradient(180deg, var(--navy) 0%, var(--navy) 72%, #124d45 88%, var(--green-deep) 100%);
  }
  .hero-photo {
    position: absolute;
    inset: 0 0 auto 0;
    height: 402px;
    background: linear-gradient(180deg, var(--photo-dark) 0%, var(--photo-mid) 50%, #8f8780 78%, var(--photo-light) 100%);
  }
  .scallop {
    position: absolute;
    left: 0;
    width: 100%;
    height: 8px;
    background-repeat: repeat-x;
    background-size: 10px 8px;
  }
  .card--front .scallop {
    top: 396px;
    background-image: radial-gradient(circle at 5px 9px, var(--navy) 4.5px, transparent 5px);
  }
  .brand {
    position: absolute;
    top: 26px;
    left: 22px;
    display: flex;
    align-items: center;
    gap: 7px;
    color: var(--white);
  }
  .brand__dot {
    width: 30px;
    height: 30px;
    border: 1.5px solid var(--white);
    border-radius: 50%;
  }
  .brand__name {
    font-weight: 700;
    font-size: 14px;
    line-height: 1;
    text-transform: uppercase;
  }
  .drink-title {
    position: absolute;
    top: 416px;
    width: 100%;
    text-align: center;
    font-family: "Merriweather", Georgia, serif;
    font-style: italic;
    font-weight: 900;
    font-size: 37px;
    color: var(--white);
  }
  .drink-story {
    position: absolute;
    top: 472px;
    left: 21px;
    right: 19px;
    font-size: 11.6px;
    line-height: 13.6px;
    letter-spacing: -0.35px;
    text-align: justify;
    color: var(--white);
  }

  /* ---------- Back ---------- */
  .card--back { background: var(--white); }
  .back-top {
    position: absolute;
    inset: 0 0 auto 0;
    height: 293px;
    background: linear-gradient(180deg, var(--green) 0%, #0d5a48 35%, #0e1d1f 70%, var(--ink) 100%);
  }
  .card--back .scallop {
    top: 293px;
    background-image: radial-gradient(circle at 5px -1px, var(--ink) 4.5px, transparent 5px);
  }
  .section-title {
    position: absolute;
    left: 23px;
    font-family: "Merriweather", Georgia, serif;
    font-style: italic;
    font-weight: 700;
    font-size: 21px;
  }
  .section-title::after {
    content: "";
    position: absolute;
    left: 0;
    top: 40px;
    width: 39px;
    height: 3px;
  }
  .section-title--ingredients { top: 22px; color: var(--white); }
  .section-title--ingredients::after { background: var(--white); }
  .section-title--instructions { top: 318px; color: var(--text-dark); }
  .section-title--instructions::after { background: var(--mint); }
  .ingredients {
    position: absolute;
    top: 78px;
    left: 23px;
    width: 197px;
    list-style: none;
    color: var(--white);
  }
  .ingredients li {
    height: 36px;
    display: flex;
    align-items: center;
    font-size: 11px;
    letter-spacing: -0.25px;
    border-bottom: 0.8px solid var(--rule);
    white-space: nowrap;
  }
  .ingredients li:last-child { border-bottom: none; }
  .ingredients em {
    font-weight: 500;
    width: 49px;
    flex: none;
  }
  .arch-frame {
    position: absolute;
    top: 21px;
    left: 237px;
    width: 150px;
    height: 340px;
    border: 2.5px solid var(--white);
    border-bottom: none;
    border-radius: 75px 75px 0 0;
    overflow: hidden;
  }
  .arch-photo {
    width: 100%;
    height: 100%;
    background: linear-gradient(180deg, #0e0d0c 0%, #2a2522 50%, #3b312a 100%);
  }
  .steps {
    position: absolute;
    top: 377px;
    left: 23px;
    width: 320px;
    list-style: none;
    color: var(--text-dark);
    font-size: 11px;
    letter-spacing: -0.25px;
  }
  .steps li {
    display: flex;
    line-height: 25px;
  }
  .steps li span:first-child { width: 20px; flex: none; }
  .sign-off {
    position: absolute;
    left: 293px;
    top: 470px;
    width: 100px;
    display: flex;
    flex-direction: column;
    align-items: center;
    gap: 6px;
  }
  .sign-off__dot {
    width: 44px;
    height: 44px;
    border-radius: 50%;
    border: 2px solid var(--mint);
  }
  .sign-off__name {
    font-weight: 700;
    font-size: 10px;
    text-transform: uppercase;
    color: var(--text-dark);
    white-space: nowrap;
  }
</style>
</head>
<body>

  <article class="card card--front">
    <div class="hero-photo" role="img" aria-label="Photo: layered café mocha in a tall glass on a saucer, dusted with cocoa, on a café counter"></div>
    <div class="scallop"></div>
    <div class="brand">
      <span class="brand__dot"></span>
      <span class="brand__name">Ember &amp;<br>Ascend</span>
    </div>
    <h1 class="drink-title">Café Mocha Bliss</h1>
    <p class="drink-story">Indulge in the balance of bittersweet espresso entwined with rich chocolate syrup to enjoy the luxe texture of the Café Mocha Bliss. Gently pour the espresso into your favorite mug, caress it with the velvety touch of chocolate, and crown the mix with steamed milk as soft as clouds. End with a swirl of whipped cream, graced with a sprinkling of chocolate shavings or a delicate dusting of cocoa powder—your canvas of comfort</p>
  </article>

  <article class="card card--back">
    <div class="back-top"></div>
    <div class="scallop"></div>
    <h2 class="section-title section-title--ingredients">Ingredients:</h2>
    <ul class="ingredients">
      <li><em>Step-1</em>5g E&amp;A Classic Black Coffee</li>
      <li><em>Step-2</em>8oz hot water</li>
      <li><em>Step-3</em>2 tablespoons chocolate syrup</li>
      <li><em>Step-4</em>Steamed milk</li>
      <li><em>Step-5</em>Whipped cream</li>
      <li><em>Step-6</em>Chocolate shavings for garnish</li>
    </ul>
    <div class="arch-frame">
      <div class="arch-photo" role="img" aria-label="Photo: mocha in a clear glass cup with milk foam on a dark wooden table"></div>
    </div>
    <h2 class="section-title section-title--instructions">Instructions:</h2>
    <ol class="steps">
      <li><span>1-</span><span>Mix 8oz of hot water with one packet E&amp;A Classic Black<br>Instant Coffee mix well until powder is fully dissolved.</span></li>
      <li><span>2-</span><span>Pour the Coffee into a mug.</span></li>
      <li><span>3-</span><span>Stir in the chocolate syrup until well combined.</span></li>
      <li><span>4-</span><span>Top with steamed milk.</span></li>
      <li><span>5-</span><span>Add a generous dollop of whipped cream.</span></li>
      <li><span>6-</span><span>Garnish with chocolate shavings.</span></li>
    </ol>
    <div class="sign-off">
      <span class="sign-off__dot"></span>
      <span class="sign-off__name">Ember &amp; Ascend</span>
    </div>
  </article>

</body>
</html>
```